Corporate holiday party invitation

Please design a holiday party invitations that looks classy and festive for our member holiday party. The event is first class, semi-formal and needs to be conveyed as such. Please see file from last year so you can see what we are aiming for. The new wording for the invite is as follows: (please use similar fonts to the file provided)

BVK Dallas/Fort Worth
cordially invites you and a guest to the
Yearly Winter Guild Supper Soiree
on Thursday, December 16th
at 6:30pm in the evening

Merrow Tower, Lantern Club
4817 Pell Avenue, 40th floor
Dallas, TX 75288

Tickets are $100 per person and include:
open premium bar, appetizers, three course dinner
and entertainment

Holiday Cocktail Dress

Target Market(s)

middle aged corporate types

Industry/Entity Type

Event

Font styles to use
Script

Requirements
Must have
• Classy holiday feel and design elements,

```html
<!DOCTYPE html>
<html lang="en">
<head>
<meta charset="UTF-8">
<title>Holiday Party Invitation</title>
<link rel="stylesheet" href="https://fonts.googleapis.com/css2?family=Great+Vibes&family=Cormorant+Garamond:wght@500&family=Open+Sans:wght@400&display=swap">
<style>
  :root {
    --bronze: #9a6233;
    --silver-dark: #a9abae;
    --silver-light: #f4f4f4;
    --cream: #f7f1e1;
    --cream-edge: #efe4c8;
    --ink: #5b3f24;
    --ornament: #6b5031;
  }
  * { margin: 0; padding: 0; box-sizing: border-box; }
  html, body { width: 900px; height: 1200px; overflow: hidden; }
  body { background: var(--bronze); position: relative; }

  .silver-frame {
    position: absolute;
    left: 54px; top: 54px; width: 792px; height: 1092px;
    background: linear-gradient(135deg, var(--silver-dark) 0%, var(--silver-light) 30%, var(--silver-dark) 55%, var(--silver-light) 80%, var(--silver-dark) 100%);
    box-shadow: 0 2px 8px rgba(0,0,0,0.35);
  }
  .card {
    position: absolute;
    left: 78px; top: 78px; width: 744px; height: 1044px;
    background: radial-gradient(ellipse at center, #fbf8ee 0%, var(--cream) 55%, var(--cream-edge) 100%);
  }

  .corner-ornament {
    position: absolute;
    background: linear-gradient(135deg, rgba(107,80,49,0.32), rgba(107,80,49,0.10));
    border-radius: 36px;
  }
  .corner-ornament.top-left { left: 92px; top: 92px; width: 145px; height: 110px; }
  .corner-ornament.top-right { left: 668px; top: 92px; width: 142px; height: 180px; }
  .corner-ornament.bottom-left { left: 92px; top: 970px; width: 160px; height: 140px; }
  .corner-ornament.bottom-right { left: 650px; top: 970px; width: 160px; height: 140px; }

  .invitation-text {
    position: absolute;
    left: 78px; top: 0; width: 744px;
    text-align: center;
    color: var(--ink);
  }
  .title-script {
    position: absolute; left: 0; width: 100%; top: 222px;
    font-family: "Great Vibes", cursive;
    font-size: 68px; line-height: 1; font-weight: 400;
    word-spacing: 10px;
  }
  .title-serif {
    position: absolute; left: 0; width: 100%; top: 300px;
    font-family: "Cormorant Garamond", serif;
    font-size: 44px; line-height: 1; font-weight: 500;
  }
  .host-lines {
    position: absolute; left: 0; width: 100%; top: 392px;
    font-family: "Great Vibes", cursive;
    font-size: 33px; line-height: 36px;
    word-spacing: 9px;
  }
  .details {
    font-family: "Open Sans", sans-serif;
    text-transform: uppercase;
    position: absolute; left: 0; width: 100%;
  }
  .when { top: 598px; font-size: 22px; line-height: 34px; }
  .where { top: 705px; font-size: 22px; line-height: 34px; }
  .tickets { top: 858px; font-size: 15px; line-height: 22px; letter-spacing: 0.2px; }
  .dress { top: 976px; font-size: 15px; line-height: 22px; }
</style>
</head>
<body>
  <div class="silver-frame"></div>
  <div class="card"></div>

  <div class="corner-ornament top-left" role="img" aria-label="Swirling filigree flourish, top left corner"></div>
  <div class="corner-ornament top-right" role="img" aria-label="Swirling filigree flourish, top right corner"></div>
  <div class="corner-ornament bottom-left" role="img" aria-label="Swirling filigree flourish, bottom left corner"></div>
  <div class="corner-ornament bottom-right" role="img" aria-label="Swirling filigree flourish, bottom right corner"></div>

  <main class="invitation-text">
    <h1 class="title-script">Holiday Party</h1>
    <h2 class="title-serif">Invitation</h2>
    <p class="host-lines">
      BVK Dallas / Fort Worth<br>
      cordially invites you and a guest<br>
      to the<br>
      Yearly Winter Guild<br>
      Supper Soiree
    </p>
    <p class="details when">On Thursday, December 16th<br>at 6:30pm in the evening</p>
    <p class="details where">Merrow Tower, Lantern Club<br>4817 Pell Avenue, 40th floor<br>Dallas, TX 75288</p>
    <p class="details tickets">Tickets are $100 per person and include:<br>open premium bar, appetizers, three course dinner<br>and entertainment</p>
    <p class="details dress">Holiday Cocktail Dress</p>
  </main>
</body>
</html>
```